Business Card design for Property Developer

We need a business card design for a Melbourne based Property Developer called "Kestrelmoor Holdings Pty Ltd".

We subdivide land and onsell to builders etc.

We already have a company logo, which is attached. Also I have attached the layout requirements from the printer. We would like a 2-sided design with one side displaying our logo by itself and the other with the required info, such as name, address, tel no., email, abn etc. The card will need to be used by 4 members of staff so name and contact details should be interchangable.
Updates

If possible, can you please write "name' "job position" "phone" "email" "address" on the card but leave them so I can add the details at a later time. Thank you. Also I plan on printing with UV spot printing as a background on the card. Keep this is mind when designing.

Thanks again.

Hello designers, please do not include pics of houses, house plansĀ or construction machinery etc as we really do not like the way it looks. Thank you.

Target Market(s)

Real Estate Agents, Land Owners, Local Council Departments, Govt Bodies, other Developers etc.

Industry/Entity Type

Business

Requirements
Must have
• 2-sided design with one side displaying our logo by itself and the other with the required info, such as name, address, tel no., email, abn etc.

```html
<!DOCTYPE html>
<html lang="en">
<head>
<meta charset="utf-8">
<title>Kestrelmoor Holdings – Business Card</title>
<link href="https://fonts.googleapis.com/css2?family=Jost:wght@500;700;800&display=swap" rel="stylesheet">
<style>
  :root {
    --page: #ffffff;
    --card: #050505;
    --stripe: rgba(255, 255, 255, 0.07);
    --accent-red: #e5202b;
    --accent-blue: #2f7fd6;
  }
  html, body {
    margin: 0;
    padding: 0;
    width: 1200px;
    height: 900px;
    overflow: hidden;
    background: var(--page);
  }
  .canvas {
    position: relative;
    width: 1200px;
    height: 900px;
  }
  .card {
    position: absolute;
    top: 150px;
    width: 447px;
    height: 702px;
    background-color: var(--card);
    background-image: repeating-linear-gradient(
      -60deg,
      transparent 0,
      transparent 11px,
      var(--stripe) 11px,
      var(--stripe) 12px
    );
    font-family: "Jost", "Futura", sans-serif;
    color: var(--accent-red);
    text-transform: uppercase;
  }
  .card--info { left: 94px; }
  .card--brand { left: 640px; }

  .info-address {
    position: absolute;
    right: 40px;
    top: 312px;
    margin: 0;
    text-align: right;
    font-weight: 800;
    font-size: 17px;
    line-height: 21px;
    letter-spacing: 0.2px;
  }
  .info-mark {
    position: absolute;
    right: 40px;
    top: 430px;
    display: flex;
    flex-direction: column;
    align-items: flex-end;
    gap: 10px;
  }
  .info-mark__circle {
    width: 100px;
    height: 100px;
    border-radius: 50%;
    border: 10px solid var(--accent-blue);
    box-sizing: border-box;
  }
  .info-mark__name {
    font-weight: 700;
    font-size: 14px;
    letter-spacing: 1px;
  }
  .info-contact {
    position: absolute;
    right: 40px;
    top: 615px;
    margin: 0;
    text-align: right;
    font-weight: 500;
    font-size: 16px;
    line-height: 21px;
  }

  .brand-mark {
    position: absolute;
    left: 0;
    right: 0;
    top: 270px;
    display: flex;
    flex-direction: column;
    align-items: center;
    gap: 18px;
  }
  .brand-mark__circle {
    width: 104px;
    height: 104px;
    border-radius: 50%;
    border: 11px solid var(--accent-blue);
    box-sizing: border-box;
  }
  .brand-mark__name {
    font-weight: 800;
    font-size: 30px;
    letter-spacing: 1px;
    line-height: 1;
    text-align: center;
  }
</style>
</head>
<body>
<main class="canvas">
  <section class="card card--info" aria-label="Card back with contact details">
    <p class="info-address">48 Larkspur Lane<br>Melbourne VIC 3000</p>
    <div class="info-mark">
      <div class="info-mark__circle"></div>
      <span class="info-mark__name">Kestrelmoor Holdings</span>
    </div>
    <p class="info-contact">Alex Reed :: Job Position<br>email@kestrelmoor.com</p>
  </section>

  <section class="card card--brand" aria-label="Card front with company name">
    <div class="brand-mark">
      <div class="brand-mark__circle"></div>
      <span class="brand-mark__name">Kestrelmoor<br>Holdings</span>
    </div>
  </section>
</main>
</body>
</html>
```